Need Letterhead Design & Matching Business Card

I have a logo that I love already. But the letterhead is less than appealing and boring. I'd like a design for my letterhead which I will match with business cards. Also, I'd like to have used fonts that are generally available, as my current letterhead uses a font named "SPACE" which nobody has unless they download it...so when a Word version is forwarded, it looks awful on the receiver's screed due to not having the font. That being said, modern is the look we like and are going for.

My business is "Halloran Brightmoor PC" - a law firm specializing in representing people who have suffered catastrophic injuries or death (plane, auto, train crashes etc.).

See attached letterhead, which has all of the pertinent information. My logo is also attached in various formats.

```html
<!DOCTYPE html>
<html lang="en">
<head>
<meta charset="utf-8">
<title>Halloran Brightmoor PC — Letterhead &amp; Business Cards</title>
<link href="https://fonts.googleapis.com/css2?family=Source+Sans+3:wght@300;400;600&display=swap" rel="stylesheet">
<style>
  :root {
    --backdrop: #ececec;
    --paper: #ffffff;
    --ink: #3a3a3a;
    --ink-soft: #5c5c5c;
    --mark: #2b2b2b;
    --card-dark: #1f1f1f;
    --card-dark-text: #8a8a8a;
    --rule: #9a9a9a;
    --signature: #c9cdd8;
  }
  * { box-sizing: border-box; margin: 0; padding: 0; }
  html, body { width: 1200px; height: 795px; overflow: hidden; }
  body {
    background: var(--backdrop);
    font-family: "Source Sans 3", Arial, sans-serif;
    color: var(--ink);
    position: relative;
  }

  /* Letterhead */
  .letterhead {
    position: absolute; left: 70px; top: 30px;
    width: 520px; height: 735px;
    background: var(--paper);
    box-shadow: 0 2px 8px rgba(0,0,0,.12);
    padding: 56px 62px 40px 62px;
  }
  .brand { display: flex; align-items: center; gap: 10px; }
  .brand-square { width: 34px; height: 34px; background: var(--mark); flex: none; }
  .brand-name {
    font-weight: 300; letter-spacing: .14em; text-transform: uppercase;
    color: var(--mark); line-height: 1.05;
  }
  .letterhead .brand { justify-content: center; margin-bottom: 70px; }
  .letterhead .brand-name { font-size: 16px; }

  .letter-body { font-size: 9.6px; line-height: 1.5; color: var(--ink-soft); }
  .letter-body p { margin-bottom: 12px; }
  .salutation { margin-bottom: 10px !important; }
  .closing { margin-top: 4px; }
  .signature {
    width: 90px; height: 52px; margin-top: 8px;
    background: var(--signature); border-radius: 4px;
  }

  .letter-footer {
    position: absolute; right: 50px; bottom: 40px;
    text-align: right; font-size: 11px; color: var(--ink); line-height: 1.6;
  }
  .contact-row { display: inline-flex; align-items: center; gap: 4px; margin-left: 8px; }
  .icon { width: 10px; height: 10px; fill: var(--ink); }

  /* Business cards */
  .card {
    position: absolute; width: 336px; height: 192px;
    box-shadow: 0 2px 8px rgba(0,0,0,.15);
  }
  .card-front {
    left: 720px; top: 470px; background: var(--paper);
    padding: 22px 24px;
  }
  .card-front .brand { justify-content: flex-end; gap: 7px; }
  .card-front .brand-square { width: 22px; height: 22px; }
  .card-front .brand-name { font-size: 10.5px; }
  .card-rule { height: 1px; background: var(--rule); margin: 14px 0 12px; }
  .card-details { display: flex; justify-content: space-between; font-size: 9px; color: var(--ink-soft); line-height: 1.45; }
  .holder-name { font-weight: 600; font-size: 10.5px; color: var(--ink); letter-spacing: .03em; text-transform: uppercase; }
  .holder-title { margin-bottom: 8px; }
  .card-contact { display: flex; align-items: center; gap: 5px; }
  .card-contact .icon { width: 8px; height: 8px; fill: var(--ink-soft); }
  .card-address { text-align: right; }

  .card-back {
    left: 760px; top: 160px; background: var(--card-dark);
    display: flex; align-items: center; justify-content: center;
  }
  .card-back .brand-square { width: 30px; height: 30px; background: #4a4a4a; }
  .card-back .brand-name { font-size: 14px; color: var(--card-dark-text); }
</style>
</head>
<body>

<main class="letterhead">
  <header class="brand">
    <span class="brand-square"></span>
    <span class="brand-name">Halloran<br>Brightmoor PC</span>
  </header>

  <section class="letter-body">
    <p class="salutation">Dear customer,</p>
    <p>Lorem ipsum dolor sit amet, consectetur adipisicing elit, sed do eiusmod tempor incididunt ut labore et dolore magna aliqua. Ut enim ad minim veniam, quis nostrud exercitation ullamco laboris nisi ut aliquip ex ea commodo consequat. Duis aute irure dolor in reprehenderit in voluptate velit esse cillum dolore eu fugiat nulla pariatur. Excepteur sint occaecat cupidatat non proident, sunt in culpa qui officia deserunt mollit anim id est laborum.</p>
    <p>Lorem ipsum dolor sit amet, consectetur adipisicing elit, sed do eiusmod tempor incididunt ut labore et dolore magna aliqua. Ut enim ad minim veniam, quis nostrud exercitation ullamco laboris nisi ut aliquip ex ea commodo consequat. Duis aute irure dolor in reprehenderit in voluptate velit esse cillum dolore eu fugiat nulla pariatur. Excepteur sint occaecat cupidatat non proident, sunt in culpa qui officia deserunt mollit anim id est laborum.</p>
    <p>Lorem ipsum dolor sit amet, consectetur adipisicing elit, sed do eiusmod tempor incididunt ut labore et dolore magna aliqua. Ut enim ad minim veniam, quis nostrud exercitation ullamco laboris nisi ut aliquip ex ea commodo consequat. Duis aute irure dolor in reprehenderit in voluptate velit esse cillum dolore eu fugiat nulla pariatur. Excepteur sint occaecat cupidatat non proident, sunt in culpa qui officia deserunt mollit anim id est laborum.</p>
    <p>Lorem ipsum dolor sit amet, consectetur adipisicing elit, sed do eiusmod tempor incididunt ut labore et dolore magna aliqua. Ut enim ad minim veniam, quis nostrud exercitation ullamco laboris nisi ut aliquip ex ea commodo consequat. Duis aute irure dolor in reprehenderit.</p>
    <p class="closing">Yours Sincerely,</p>
    <div class="signature" role="img" aria-label="Handwritten signature"></div>
  </section>

  <footer class="letter-footer">
    <div>4820 Marlowe Ave. Suite 1200 Westbrook, CA 90317</div>
    <div>
      <span class="contact-row"><svg class="icon" viewBox="0 0 10 10"><path d="M2 1l2 0 .6 2-1.2 .8a5 5 0 0 0 2.8 2.8L7 5.4l2 .6v2L8 9C4 9 1 6 1 2z"/></svg>855-555-0142</span>
      <span class="contact-row"><svg class="icon" viewBox="0 0 10 10"><path d="M0 2h10v6H0z M0 2l5 3.5L10 2" stroke="#fff" stroke-width=".8"/></svg>info@halloranbrightmoor.com</span>
      <span class="contact-row"><svg class="icon" viewBox="0 0 10 10"><circle cx="5" cy="5" r="4.5"/></svg>www.halloranbrightmoor.com</span>
    </div>
  </footer>
</main>

<section class="card card-back">
  <div class="brand">
    <span class="brand-square"></span>
    <span class="brand-name">Halloran<br>Brightmoor PC</span>
  </div>
</section>

<section class="card card-front">
  <div class="brand">
    <span class="brand-square"></span>
    <span class="brand-name">Halloran<br>Brightmoor PC</span>
  </div>
  <div class="card-rule"></div>
  <div class="card-details">
    <div class="card-person">
      <div class="holder-name">Daniel R. Ostrander</div>
      <div class="holder-title">Founder &amp; CEO</div>
      <div class="card-contact"><svg class="icon" viewBox="0 0 10 10"><path d="M2 1l2 0 .6 2-1.2 .8a5 5 0 0 0 2.8 2.8L7 5.4l2 .6v2L8 9C4 9 1 6 1 2z"/></svg>855-555-0142</div>
      <div class="card-contact"><svg class="icon" viewBox="0 0 10 10"><path d="M0 2h10v6H0z"/></svg>info@halloranbrightmoor.com</div>
      <div class="card-contact"><svg class="icon" viewBox="0 0 10 10"><circle cx="5" cy="5" r="4.5"/></svg>www.halloranbrightmoor.com</div>
    </div>
    <div class="card-address">
      4820 Marlowe Ave.<br>Suite 1200<br>Westbrook, CA 90317
    </div>
  </div>
</section>

</body>
</html>
```